New London based construction company website

We need a website designing for our new London based construction company which aims to provide total & fernway yard services.

The website is to have two sides to it one for "halcrest build services" and one for "fernway yard services" with an opening page with both logo's to choose from.

Would like the website to be modern, professional and inspire confidence.

Target Market(s)

Those specifically visiting the site to check that the company is professional

Industry/Entity Type

Construction

Contact Information for Business Card

One side for Fernway Yard Services the other Halcrest Build Services

Number of Pages Required

5+ page

Font styles to use
Sans Serif

Requirements
Must have
• The website is to have two sides to it one for "halcrest build services" and one for "fernway yard services" with an opening page with both logo's to choose from.

```html
<!DOCTYPE html>
<html lang="en">
<head>
<meta charset="utf-8">
<title>Fernway Yard Services</title>
<link rel="stylesheet" href="https://fonts.googleapis.com/css2?family=Poppins:wght@300;400;500;600&display=swap">
<style>
:root{
  --brand:#0c5a96;
  --ink:#111;
  --body:#6b6b6b;
  --soft:#f9f9f9;
  --line:#cfcfcf;
  --white:#fff;
}
*{margin:0;padding:0;box-sizing:border-box}
html,body{width:1200px;height:2296px;overflow:hidden;background:var(--white)}
body{position:relative;font-family:'Poppins',sans-serif;color:var(--ink)}
.abs{position:absolute}
.brand{display:flex;align-items:center;gap:10px}
.brand-mark{width:24px;height:24px;background:var(--brand)}
.brand-name{font-size:17px;font-weight:500;color:var(--brand);letter-spacing:.5px}
.site-header{left:0;top:0;width:1200px;height:73px;background:var(--white)}
.site-header .brand{left:245px;top:22px}
.nav{left:584px;top:26px;display:flex;gap:27px;font-size:14px;font-weight:500}
.nav a{color:var(--ink);text-decoration:none;padding-bottom:9px}
.nav a.active{border-bottom:3px solid var(--brand)}
.hero{left:0;top:73px;width:1200px;height:516px;background:linear-gradient(180deg,#2b2d33 0%,#3f3a38 45%,#7a5030 78%,#2a2421 100%)}
.hero-title{left:0;width:1200px;top:280px;text-align:center;color:var(--white);font-size:43px;font-weight:500}
.hero-sub{left:0;width:1200px;top:344px;text-align:center;color:var(--white);font-size:21px;font-weight:300}
.btn-ghost{display:flex;align-items:center;justify-content:center;font-size:13px;font-weight:500;text-transform:uppercase}
.hero-btn{left:520px;top:399px;width:160px;height:45px;border:1px solid #e6e6e6;color:var(--white)}
.dots{left:564px;top:516px;display:flex;gap:13px}
.dots span{width:8px;height:8px;border-radius:50%;background:var(--white)}
.dots span.on{background:#2f8fe0}
.section-title{left:0;width:1200px;text-align:center;font-size:25px;font-weight:400;color:var(--ink)}
.title-bar{left:556px;width:88px;height:6px;background:var(--brand)}
.intro-text{left:290px;top:742px;width:620px;text-align:center;font-size:10px;line-height:20px;color:var(--body)}
.intro-btn{left:534px;top:852px;width:132px;height:45px;border:1px solid var(--line);color:#444}
.services{left:0;top:960px;width:1200px;height:402px;background:var(--soft)}
.service{width:230px;top:1128px}
.service h3{display:flex;align-items:center;gap:12px;font-size:21px;font-weight:400;color:var(--ink);height:30px}
.service p{margin-top:34px;font-size:10px;line-height:20px;color:var(--body)}
.btn-solid{display:inline-flex;align-items:center;justify-content:center;margin-top:19px;width:88px;height:29px;background:var(--brand);color:var(--white);font-size:8px;font-weight:600;text-transform:uppercase}
.news-photo{top:1561px;width:346px;height:184px}
.news-date{top:1756px;font-size:12px;font-weight:500;color:#6b6b6b}
.news-text{top:1782px;width:340px;font-size:13px;line-height:20px;color:#555}
.testimonial{left:0;top:1978px;width:1200px;height:257px;background:var(--soft)}
.avatar{left:528px;top:1906px;width:144px;height:144px;border-radius:50%;border:4px solid var(--brand);background:var(--white);padding:5px}
.avatar div{width:100%;height:100%;border-radius:50%;background:linear-gradient(180deg,#9fc4df 0%,#c9a46a 55%,#4e6b8c 100%)}
.person{left:0;width:1200px;top:2058px;text-align:center;font-size:16px;font-weight:600;color:var(--brand)}
.quote{left:240px;top:2100px;width:720px;text-align:center;font-size:9.6px;line-height:20px;color:#555}
.site-footer .brand{left:245px;top:2254px}
.copyright{left:650px;width:304px;top:2263px;text-align:right;font-size:10px;color:#888}
</style>
</head>
<body>
<header class="site-header abs">
  <div class="brand abs"><span class="brand-mark"></span><span class="brand-name">Fernway Yard Services</span></div>
  <nav class="nav abs"><a class="active">Home</a><a>About Us</a><a>Services</a><a>FAQ's</a><a>Contact&nbsp; Us</a></nav>
</header>

<section class="hero abs" role="img" aria-label="Construction workers silhouetted against a sunset sky between tower cranes and rebar"></section>
<h1 class="hero-title abs">Fernway Yard Services</h1>
<p class="hero-sub abs">We provide total &amp; fernway yard services.</p>
<div class="hero-btn btn-ghost abs">Learn More</div>
<div class="dots abs"><span class="on"></span><span></span><span></span><span></span></div>

<h2 class="section-title abs" style="top:657px">Welcome to Fernway Yard Services</h2>
<div class="title-bar abs" style="top:710px"></div>
<p class="intro-text abs">Sed ut perspiciatis unde omnis iste natus error sit voluptatem accusantium doloremque laudantium, totam rem aperiam, eaque ipsa quae ab illo inventore veritatis et quasi architecto beatae vitae dicta sunt explicabo. Nemo enim ipsam voluptatem quia voluptas sit aspernatur aut odit aut fugit, sed quia consequuntur magni dolores eos qui ratione voluptatem sequi nesciunt. Neque porro quisquam est, qui dolorem ipsum quia dolor sit amet, consectetur</p>
<div class="intro-btn btn-ghost abs">Learn More</div>

<section class="services abs"></section>
<h2 class="section-title abs" style="top:1021px">Our Services</h2>
<div class="title-bar abs" style="top:1074px"></div>

<div class="service abs" style="left:245px">
  <h3><svg width="22" height="22" viewBox="0 0 22 22" fill="none" stroke="#0c5a96" stroke-width="1.6"><rect x="3" y="7" width="6" height="13"/><rect x="9" y="3" width="8" height="17"/><path d="M12 7h2M12 11h2M12 15h2M5 11h2M5 15h2"/></svg>Corporate</h3>
  <p>Sed ut perspiciatis unde omnis iste natus error sit voluptatem accusantium doloremque laudantium, totam rem aperiam</p>
  <span class="btn-solid">Learn More</span>
</div>
<div class="service abs" style="left:488px">
  <h3><svg width="20" height="22" viewBox="0 0 20 22" fill="none" stroke="#0c5a96" stroke-width="1.6"><rect x="2" y="2" width="16" height="18"/><path d="M6 6h2M12 6h2M6 10h2M12 10h2M6 14h2M12 14h2"/></svg>Cormmercial</h3>
  <p>Sed ut perspiciatis unde omnis iste natus error sit voluptatem accusantium doloremque laudantium, totam rem aperiam</p>
  <span class="btn-solid">Learn More</span>
</div>
<div class="service abs" style="left:732px">
  <h3><svg width="22" height="22" viewBox="0 0 22 22" fill="none" stroke="#0c5a96" stroke-width="1.6"><path d="M2 11L11 3l9 8M5 9v11h12V9"/><rect x="9" y="14" width="4" height="6"/></svg>Residential</h3>
  <p>Sed ut perspiciatis unde omnis iste natus error sit voluptatem accusantium doloremque laudantium, totam rem aperiam</p>
  <span class="btn-solid">Learn More</span>
</div>

<h2 class="section-title abs" style="top:1448px">Latest News</h2>
<div class="title-bar abs" style="top:1501px"></div>

<div class="news-photo abs" style="left:245px;background:linear-gradient(180deg,#a8d4c4 0%,#e8c27a 60%,#3a2a1c 100%)" role="img" aria-label="Workers silhouetted on steel rebar framework at sunrise"></div>
<p class="news-date abs" style="left:245px">March 30th 2016</p>
<p class="news-text abs" style="left:245px">Sed ut perspiciatis unde omnis iste natus error sit voluptatem accusantium doloremque...</p>

<div class="news-photo abs" style="left:608px;background:linear-gradient(180deg,#d9b48c 0%,#e8d8c6 50%,#6b5a4c 100%)" role="img" aria-label="Two engineers in hard hats reviewing plans beside scaffolding"></div>
<p class="news-date abs" style="left:608px">March 30th 2016</p>
<p class="news-text abs" style="left:608px">Sed ut perspiciatis unde omnis iste natus error sit voluptatem accusantium doloremque...</p>

<section class="testimonial abs"></section>
<div class="avatar abs"><div role="img" aria-label="Portrait of a site engineer in a yellow hard hat"></div></div>
<p class="person abs">Daniel Ostrow</p>
<p class="quote abs">Sed ut perspiciatis unde omnis iste natus error sit voluptatem accusantium doloremque laudantium, totam rem aperiam, eaque ipsa quae ab illo inventore veritatis et quasi architecto beatae vitae dicta sunt explicabo. Nemo enim ipsam voluptatem quia voluptas sit aspernatur aut odit aut fugit, sed quia consequuntur magni dolores eos qui ratione voluptatem sequi nesciunt. Neque porro quisquam est, qui dolorem</p>

<footer class="site-footer">
  <div class="brand abs"><span class="brand-mark"></span><span class="brand-name">Fernway Yard Services</span></div>
  <p class="copyright abs">© 2017 Company Name &nbsp;|&nbsp; All Rights Reserved</p>
</footer>
</body>
</html>
```